" Não vendemos nossos serviços "no varejo". Somos chamados a participar de projetos de investimento no Brasil ainda na fase de concepção, sob acordo de confidencialidade, buscando alimentar a modelagem financeira com os inputs tributários que frequentemente são cruciais na definição de viabilidade do projeto. Também somos chamados por nossos clientes para avaliar ou alocar contratualmente riscos decorrentes de contingências fiscais, especialmente em fusões e aquisições de empresas. E, ainda, patrocinar defesas ou pleitos em processos administrativos ou judiciais, sempre tendo como parte adversária o fisco (federal, estadual ou municipal). Atuamos em um ambiente profissional onde ética, compliance, qualidade e comprometimento são premissas. O propósito de nossa empresa é a criação de valor de modo sustentável, em questões fiscais, para negócios empreendidos no Brasil. "

```html
<!DOCTYPE html>
<html lang="pt-BR">
<head>
<meta charset="utf-8">
<title>Cartão de visita – Moreira Lins Tavares Advogados</title>
<link rel="stylesheet" href="https://fonts.googleapis.com/css2?family=Open+Sans:wght@400;600&display=swap">
<style>
  :root {
    --page: #ebe8e4;
    --card: #ffffff;
    --navy: #1f1f5e;
    --accent: #7f93c9;
    --ink: #1a1a3a;
    --faint: #e4e6ea;
  }
  html, body {
    margin: 0;
    width: 1200px;
    height: 1200px;
    overflow: hidden;
    background: var(--page);
    font-family: "Open Sans", Arial, sans-serif;
  }
  .business-card {
    position: absolute;
    left: 110px;
    top: 469px;
    width: 980px;
    height: 262px;
    background: var(--card);
    border-radius: 16px;
    overflow: hidden;
    box-shadow: 0 6px 18px rgba(0,0,0,0.18);
  }
  .card-shapes {
    position: absolute;
    inset: 0;
  }
  .brand-name {
    position: absolute;
    left: 40px;
    top: 0;
    width: 360px;
    height: 262px;
    display: flex;
    align-items: center;
    justify-content: center;
    text-align: center;
    color: #ffffff;
    font-weight: 600;
    font-size: 34px;
    line-height: 1.2;
    letter-spacing: 1px;
  }
  .firm-watermark {
    position: absolute;
    left: 610px;
    top: 22px;
    margin: 0;
    color: var(--faint);
    font-size: 40px;
    font-weight: 400;
    line-height: 52px;
    letter-spacing: 3px;
    text-transform: uppercase;
  }
  .person-name {
    position: absolute;
    left: 540px;
    top: 16px;
    margin: 0;
    color: var(--ink);
    font-size: 31px;
    font-weight: 400;
  }
  .contact-list {
    position: absolute;
    left: 542px;
    top: 80px;
    margin: 0;
    padding: 0;
    list-style: none;
  }
  .contact-item {
    display: flex;
    align-items: center;
    height: 30px;
    margin-bottom: 14px;
    color: var(--ink);
    font-size: 20px;
  }
  .contact-item:nth-child(2) { margin-bottom: 18px; }
  .contact-item:nth-child(3) { margin-bottom: 20px; }
  .contact-icon {
    width: 22px;
    height: 22px;
    margin-right: 14px;
    flex: none;
  }
</style>
</head>
<body>
  <div class="business-card">
    <svg class="card-shapes" viewBox="0 0 980 262" width="980" height="262" aria-hidden="true">
      <path d="M0 0 H525 C480 70 445 160 446 262 H0 Z" fill="var(--accent)"/>
      <path d="M0 0 H470 C440 70 420 170 428 262 H0 Z" fill="var(--navy)"/>
    </svg>

    <div class="brand-name">Moreira Lins<br>Tavares</div>

    <p class="firm-watermark">Moreira<br>Lins<br>Tavares<br>Advogados</p>

    <h1 class="person-name">Nome Completo</h1>

    <ul class="contact-list">
      <li class="contact-item">
        <svg class="contact-icon" viewBox="0 0 22 22" aria-hidden="true">
          <circle cx="11" cy="11" r="10" fill="none" stroke="var(--ink)" stroke-width="2"/>
        </svg>
        (00) 0000-0000
      </li>
      <li class="contact-item">
        <svg class="contact-icon" viewBox="0 0 22 22" aria-hidden="true">
          <path d="M2 8 C2 4 20 4 20 8 L16 9 L15 7 H7 L6 9 Z" fill="var(--ink)"/>
          <path d="M6 10 H16 L19 18 H3 Z" fill="var(--ink)"/>
          <circle cx="11" cy="14" r="2.2" fill="#fff"/>
        </svg>
        (00) 0000-0000
      </li>
      <li class="contact-item">
        <svg class="contact-icon" viewBox="0 0 22 22" aria-hidden="true">
          <circle cx="11" cy="11" r="9.5" fill="none" stroke="var(--ink)" stroke-width="1.8"/>
          <ellipse cx="11" cy="11" rx="4" ry="9.5" fill="none" stroke="var(--ink)" stroke-width="1.5"/>
          <line x1="1.5" y1="11" x2="20.5" y2="11" stroke="var(--ink)" stroke-width="1.5"/>
        </svg>
        www.seusite.com.br
      </li>
      <li class="contact-item">
        <svg class="contact-icon" viewBox="0 0 22 22" aria-hidden="true">
          <circle cx="11" cy="11" r="10" fill="none" stroke="var(--ink)" stroke-width="2"/>
        </svg>
        @nome daempresa
      </li>
    </ul>
  </div>
</body>
</html>
```